Unique name card for Travel Agency

We provide domestic and international airline ticketing, hotel bookings and tour packages to exciting destinations in the Philippines and beyond.

Our motto: Explore, Discover, Dream.

With over 300 airlines, 100 destinations and 100,000 hotel partners worldwide, we are poised to increase our market share of the competitive travel industry.

Target Market(s)

international travelers

Industry/Entity Type

Travel Industry

Contact Information for Business Card

MVR JOURNEYS N SERVICES
address:
Lorenzana Building, Mabini Road,Tabon
Marisol, Valcarra 5712, Philippines

Name: Nora Valdestre
General Manager
Tel: 036 415 8270
Mobile: 0920 613 5097 (BRISK)
0917 952 3048 (ORBIX)
Facebook: facebook.com/mvrjourneys
email: support@mvrjourneys.com
website: www.mvrjourneys.com

Font styles to use
Serif

Requirements
Must have
• different airline logos: Islas Skyways, Luzon Azure, Jetvia, Falconfly, Meridian Airlines, Orient Airlines, Hanbit Air, Albion Skyways Solvane Coastal, Sirilune Air, Novadel, Ilowen Air
• Back of name card: Explore. Discover. Dream
• 300 Airlines, 100 Destinations, 100,000 Hotel Partners
Nice to have
• colours that compliment our logo
Should not have
• boring templates which are so common

```html
<!DOCTYPE html>
<html lang="en">
<head>
<meta charset="utf-8">
<title>MVR Journeys — Business Card</title>
<link rel="stylesheet" href="https://fonts.googleapis.com/css2?family=Archivo+Black&family=Questrial&family=Raleway:wght@700&display=swap">
<style>
  :root {
    --page-bg: #ececec;
    --card-white: #ffffff;
    --brand-red: #e3344e;
    --brand-red-deep: #b3202f;
    --brand-teal: #1fa99a;
    --ink: #4a4a4a;
    --rule: #9a9a9a;
  }
  * { box-sizing: border-box; margin: 0; padding: 0; }
  html, body {
    width: 1200px; height: 1200px; overflow: hidden;
    background: var(--page-bg);
  }
  body { position: relative; font-family: "Questrial", sans-serif; color: var(--ink); }

  .card {
    position: absolute; left: 120px; width: 960px; height: 548px;
    box-shadow: 0 6px 14px rgba(0,0,0,0.22);
    overflow: hidden;
  }
  .card--front { top: 36px; background: var(--card-white); }
  .card--back  { top: 616px; background: var(--brand-red); }

  /* front */
  .brand {
    position: absolute; left: 111px; top: 84px;
    display: flex; align-items: center; gap: 10px;
  }
  .brand__dot { width: 24px; height: 24px; border-radius: 50%; background: var(--brand-red); }
  .brand__name { font-family: "Questrial", sans-serif; font-size: 27px; color: var(--brand-teal); }
  .divider-accent { position: absolute; left: 478px; top: 80px; width: 3px; height: 48px; background: var(--brand-red); }
  .divider-rule   { position: absolute; left: 478px; top: 152px; width: 1px; height: 186px; background: var(--rule); }

  .person { position: absolute; left: 541px; top: 72px; }
  .person__name { font-family: "Raleway", sans-serif; font-weight: 700; font-size: 30px; color: var(--brand-red); line-height: 1.1; }
  .person__title { font-size: 21px; color: var(--ink); margin-top: 4px; }

  .company { position: absolute; left: 111px; top: 196px; font-size: 21px; line-height: 31px; }
  .company__name { font-family: "Raleway", sans-serif; font-weight: 700; color: var(--brand-red); letter-spacing: 0.3px; }

  .contacts { position: absolute; left: 541px; top: 150px; list-style: none; font-size: 21px; line-height: 31px; }
  .contacts li { display: flex; align-items: center; gap: 8px; }
  .contacts svg { width: 17px; height: 17px; flex: none; fill: var(--brand-red); }
  .contacts .social-mark { width: 12px; height: 12px; margin: 0 2px 0 3px; background: var(--brand-red); flex: none; }

  .partners {
    position: absolute; left: 90px; right: 70px; top: 398px;
    display: grid; grid-template-columns: repeat(6, 1fr);
    row-gap: 50px; column-gap: 10px; align-items: center; justify-items: center;
  }
  .partner { font-family: "Raleway", sans-serif; font-weight: 700; font-size: 16px; white-space: nowrap; }
  .partner--red { color: var(--brand-red); }
  .partner--navy { color: #1e2a5a; }
  .partner--teal { color: #1b8fb0; }
  .partner--grey { color: #3c3c3c; }
  .partner--gold { color: #c88a1b; }
  .partner--green { color: #2f7d3a; }

  .card__edge { position: absolute; left: 0; right: 0; bottom: 0; height: 7px; background: var(--brand-red); }

  /* back */
  .stats { position: absolute; left: 44px; top: 70px; color: #fff; }
  .stat { margin-bottom: 18px; }
  .stat__figure { font-size: 84px; line-height: 84px; letter-spacing: -1px; }
  .stat__label { font-size: 29px; line-height: 34px; }

  .motto {
    position: absolute; left: 460px; top: 138px; width: 470px;
    font-family: "Archivo Black", sans-serif; color: var(--brand-red-deep);
    text-transform: uppercase;
  }
  .motto span { display: block; white-space: nowrap; }
  .motto__explore  { font-size: 86px; line-height: 84px; }
  .motto__discover { font-size: 75px; line-height: 74px; }
  .motto__dream    { font-size: 110px; line-height: 104px; }
</style>
</head>
<body>

<section class="card card--front" aria-label="Business card front">
  <div class="brand">
    <span class="brand__dot"></span>
    <span class="brand__name">MVR Journeys</span>
  </div>
  <span class="divider-accent"></span>
  <span class="divider-rule"></span>

  <div class="person">
    <p class="person__name">Nora Valdestre</p>
    <p class="person__title">General Manager</p>
  </div>

  <div class="company">
    <p class="company__name">MVR JOURNEYS N SERVICES</p>
    <p>Lorenzana Building, Mabini Road,</p>
    <p>Tabon Marisol, Valcarra 5712,</p>
    <p>Philippines</p>
  </div>

  <ul class="contacts">
    <li><svg viewBox="0 0 24 24"><path d="M6.6 10.8a15 15 0 0 0 6.6 6.6l2.2-2.2c.3-.3.7-.4 1-.2 1.1.4 2.3.6 3.6.6.6 0 1 .4 1 1V20c0 .6-.4 1-1 1A17 17 0 0 1 3 4c0-.6.4-1 1-1h3.5c.6 0 1 .4 1 1 0 1.3.2 2.5.6 3.6.1.3 0 .7-.2 1z"/></svg>036 415 8270</li>
    <li><svg viewBox="0 0 24 24"><path d="M7 1h10a2 2 0 0 1 2 2v18a2 2 0 0 1-2 2H7a2 2 0 0 1-2-2V3a2 2 0 0 1 2-2zm0 3v14h10V4zm5 15.5a1 1 0 1 0 0 2 1 1 0 0 0 0-2z"/></svg>0920 613 5097 (BRISK)</li>
    <li><svg viewBox="0 0 24 24"><path d="M6.6 10.8a15 15 0 0 0 6.6 6.6l2.2-2.2c.3-.3.7-.4 1-.2 1.1.4 2.3.6 3.6.6.6 0 1 .4 1 1V20c0 .6-.4 1-1 1A17 17 0 0 1 3 4c0-.6.4-1 1-1h3.5c.6 0 1 .4 1 1 0 1.3.2 2.5.6 3.6.1.3 0 .7-.2 1z"/></svg>0917 952 3048 (ORBIX)</li>
    <li><span class="social-mark"></span>www.facebook.com/mvrjourneys</li>
    <li><svg viewBox="0 0 24 24"><path d="M2 5h20v14H2zm2 2v.5l8 5.5 8-5.5V7z"/></svg>support@mvrjourneys.com</li>
    <li><svg viewBox="0 0 24 24"><path d="M12 2a10 10 0 1 0 0 20 10 10 0 0 0 0-20zm0 2c.9 0 2.2 1.9 2.8 5H9.2C9.8 5.9 11.1 4 12 4zM4.3 11h3.8a17 17 0 0 0 0 2H4.3a8 8 0 0 1 0-2zm5.8 0h3.8a15 15 0 0 1 0 2h-3.8a15 15 0 0 1 0-2zm5.8 0h3.8a8 8 0 0 1 0 2h-3.8a17 17 0 0 0 0-2zM12 20c-.9 0-2.2-1.9-2.8-5h5.6c-.6 3.1-1.9 5-2.8 5z"/></svg>www.mvrjourneys.com</li>
  </ul>

  <div class="partners" aria-label="Airline partners">
    <span class="partner partner--navy">Islas Skyways</span>
    <span class="partner partner--navy">Albion Skyways</span>
    <span class="partner partner--teal">Luzon Azure</span>
    <span class="partner partner--red">Jetvia</span>
    <span class="partner partner--grey">Falconfly</span>
    <span class="partner partner--gold">Meridian Airlines</span>
    <span class="partner partner--grey">Sirilune Air</span>
    <span class="partner partner--navy">Hanbit Air</span>
    <span class="partner partner--navy">Novadel</span>
    <span class="partner partner--red">Orient Airlines</span>
    <span class="partner partner--teal">Solvane Coastal</span>
    <span class="partner partner--green">Ilowen Air</span>
  </div>

  <span class="card__edge"></span>
</section>

<section class="card card--back" aria-label="Business card back">
  <div class="stats">
    <div class="stat"><p class="stat__figure">300</p><p class="stat__label">Airlines</p></div>
    <div class="stat"><p class="stat__figure">100</p><p class="stat__label">Destinations Worldwide</p></div>
    <div class="stat"><p class="stat__figure">100,000</p><p class="stat__label">Hotel Partners</p></div>
  </div>
  <p class="motto">
    <span class="motto__explore">Explore</span>
    <span class="motto__discover">Discover</span>
    <span class="motto__dream">Dream</span>
  </p>
</section>

</body>
</html>
```